Staffing/Recruitment company

We need to upgrade our website. At the moment we have a template that was built last year and looks not good at all.
We would like to update it with a new design based on what is popular this year. Including some visual effects etc.
This website is to give all information to our potential clients about what we do, clients with worked in the past, how to contact us and about us.
The website consists of 4 pages.
We would like to see a design that uses the color blue.
The current website is https://brightlanestaff.us/
Logo of the company is uploaded

Some designs were not complete...

```html
<!DOCTYPE html>
<html lang="en">
<head>
<meta charset="utf-8">
<title>Brightlane Staff — Join Our Career Network</title>
<link href="https://fonts.googleapis.com/css2?family=Poppins:wght@300;400;500;600;700;800&display=swap" rel="stylesheet">
<style>
:root{
  --navy:#1c1b5c;
  --navy-deep:#14134a;
  --hero:#2c2b6b;
  --orange:#f05a28;
  --orange-soft:#e8683f;
  --ink:#1f1f3a;
  --white:#ffffff;
}
*{margin:0;padding:0;box-sizing:border-box}
html,body{width:1200px;height:3329px;overflow:hidden}
body{position:relative;background:var(--white);font-family:'Poppins',sans-serif;color:var(--ink)}
.abs{position:absolute}
svg.band{position:absolute;left:0;display:block}

/* header */
.site-header{top:0;left:0;width:1200px;height:101px;background:var(--white)}
.brand{display:flex;align-items:center;gap:10px;font-weight:700;font-size:18px;color:var(--navy);letter-spacing:.3px}
.brand-mark{width:22px;height:22px;background:var(--orange)}
.site-header .brand{left:103px;top:46px}
.nav{top:48px;font-size:12.5px;color:var(--ink);font-weight:400}
.btn{display:flex;align-items:center;justify-content:center;font-size:12.5px;font-weight:600}
.btn-contact{left:979px;top:36px;width:110px;height:38px;background:var(--orange);color:var(--white);border-radius:2px}

/* hero */
.hero-title{left:97px;top:186px;color:var(--white);line-height:1}
.hero-title .light{display:block;font-weight:300;font-size:58px;margin-bottom:16px}
.hero-title .bold{display:block;font-weight:800;font-size:72px;margin-bottom:12px}
.hero-text{left:98px;top:442px;width:470px;color:var(--white);font-size:12.5px;line-height:22px}
.btn-join{left:98px;top:531px;width:110px;height:36px;background:var(--orange);color:var(--white);border-radius:2px}

/* about */
.about-graphic{left:152px;top:756px;width:332px;height:432px;background:linear-gradient(150deg,#3c3a74 0%,#6b5a7e 45%,#e0784c 100%);clip-path:polygon(50% 0,100% 22%,100% 78%,50% 100%,0 78%,0 22%)}
.about-title{left:620px;top:848px;font-size:42px;font-weight:800;color:var(--navy)}
.about-title span{color:var(--orange)}
.about-sub{left:620px;top:909px;font-size:16px;color:var(--orange);font-weight:500}
.about-text{left:620px;top:952px;width:462px;font-size:12px;line-height:20.6px;color:var(--ink)}
.about-text p+p{margin-top:20px}

/* divisions */
.div-bg{left:0;top:1330px;width:1200px;height:492px;background:linear-gradient(180deg,#2d2c6b,#3a3a7c 50%,#2a2966)}
.div-title{left:0;width:1200px;top:1358px;text-align:center;color:var(--white);font-size:42px;font-weight:800}
.div-sub{left:0;width:1200px;top:1414px;text-align:center;color:var(--white);font-size:15px;font-weight:500}
.card{background:var(--white);text-align:center;padding-top:26px}
.card-finance{left:172px;top:1476px;width:285px;height:265px}
.card-health{left:457px;top:1460px;width:290px;height:299px;background:linear-gradient(160deg,#e9764a,#ef6333);padding-top:42px;box-shadow:0 10px 30px rgba(0,0,0,.25);color:var(--white)}
.card-gov{left:747px;top:1476px;width:283px;height:265px}
.icon-circle{width:83px;height:83px;border-radius:50%;background:var(--orange);margin:0 auto;display:flex;align-items:center;justify-content:center}
.card-health .icon-circle{background:var(--white)}
.card h3{margin-top:24px;font-size:15.5px;font-weight:500;color:var(--navy)}
.card-health h3{color:var(--white)}
.card p{margin:22px auto 0;width:240px;font-size:12px;line-height:20px}

/* services */
.svc-title{left:0;width:1200px;top:1910px;text-align:center;font-size:42px;font-weight:800;color:var(--navy)}
.svc-title span{color:var(--orange)}
.svc{top:2031px;width:290px}
.svc-photo{width:290px;height:266px}
.svc h3{margin:28px 0 0 4px;font-size:16px;line-height:26px;font-weight:500;color:var(--orange)}
.svc p{margin:24px 0 0 4px;font-size:12px;line-height:20.5px;width:270px}
.btn-more{margin:30px 0 0 4px;width:110px;height:37px;border:1px solid var(--orange);color:var(--navy);font-size:12px;font-weight:600}

/* request */
.req-left{left:0;top:2700px;width:597px;height:504px;background:linear-gradient(180deg,#2a2966,#14134a)}
.req-right{left:597px;top:2700px;width:603px;height:504px;background:var(--orange-soft)}
.req-title{left:131px;top:2828px;font-size:44px;font-weight:800;color:var(--white)}
.req-sub{left:133px;top:2895px;width:290px;font-size:12.5px;line-height:20px;color:var(--white)}
.contact-item{left:136px;display:flex;align-items:center;gap:20px;color:var(--white)}
.contact-item .pin{width:36px;height:36px;border-radius:50%;background:var(--orange);display:flex;align-items:center;justify-content:center}
.contact-item small{display:block;font-size:12px}
.contact-item strong{display:block;font-size:16px;font-weight:600}
.field{color:var(--white);font-size:12.5px;border-bottom:1px solid rgba(255,255,255,.85);padding-bottom:4px}
.btn-request{left:962px;top:3029px;width:127px;height:36px;background:var(--white);color:var(--navy);border-radius:2px}

/* footer */
.social{top:3258px;width:20px;height:20px;border-radius:50%;background:var(--orange)}
.site-footer .brand{left:497px;top:3256px;font-size:16px}
.copy{left:842px;top:3252px;font-size:12px;line-height:20px;color:var(--ink);font-weight:500}
.copy span{color:var(--orange)}
</style>
</head>
<body>

<header class="site-header abs">
  <div class="brand abs"><span class="brand-mark"></span>BRIGHTLANE STAFF</div>
  <a class="nav abs" style="left:708px">Home</a>
  <a class="nav abs" style="left:784px">About Us</a>
  <a class="nav abs" style="left:873px">Clients</a>
  <a class="btn btn-contact abs">Contact Us</a>
</header>

<!-- hero -->
<svg class="band" style="top:101px" width="1200" height="610" viewBox="0 0 1200 610">
  <defs>
    <linearGradient id="heroGrad" x1="0" y1="0" x2="1" y2="1"><stop offset="0" stop-color="#2a2a66"/><stop offset="1" stop-color="#34337a"/></linearGradient>
    <linearGradient id="photoGrad" x1="0" y1="0" x2="0" y2="1"><stop offset="0" stop-color="#3a3978"/><stop offset="0.55" stop-color="#23224f"/><stop offset="1" stop-color="#15142f"/></linearGradient>
  </defs>
  <rect width="1200" height="610" fill="url(#heroGrad)"/>
  <g role="img" aria-label="Photo of two business professionals standing in front of a night city skyline">
    <rect x="585" y="12" width="600" height="590" fill="url(#photoGrad)"/>
  </g>
  <polygon points="0,550 600,586 1200,550 1200,610 0,610" fill="var(--orange)"/>
  <polygon points="0,556 600,609 1200,556 1200,610 0,610" fill="#fff"/>
</svg>
<h1 class="hero-title abs"><span class="light">JOIN OUR</span><span class="bold">CAREER</span><span class="bold">NETWORK</span></h1>
<p class="hero-text abs">Our Career Network will enhance your job search and application process. Whether you choose to apply or just leave your information, we look forward to staying connected with you.</p>
<a class="btn btn-join abs">Join Now</a>

<!-- about -->
<div class="about-graphic abs" role="img" aria-label="Angular emblem filled with photos of people at work"></div>
<h2 class="about-title abs">ABOUT <span>US</span></h2>
<div class="about-sub abs">Who We Are</div>
<div class="about-text abs">
  <p>Day in and day out for the last years we’ve been more than just a staffing company. Throughout this time we’ve built relationships, we’ve grown together internally and externally, and have created a system that allows us to personally cater to the needs of our clients and candidates.</p>
  <p>We’ve been a mentor for some, a team builder for others, but most importantly we’ve been there. We know there is no substitute for experience, so let us help you navigate through the ever changing web of talent.</p>
</div>

<!-- divisions -->
<div class="div-bg abs" role="img" aria-label="Overhead photo of a team working at a desk with laptops, tinted blue"></div>
<svg class="band" style="top:1268px" width="1200" height="70" viewBox="0 0 1200 70">
  <polygon points="0,62 600,4 1200,69 1200,70 0,70" fill="var(--orange)"/>
  <polygon points="0,70 600,18 1200,70" fill="#2d2c6b"/>
</svg>
<h2 class="div-title abs">OUR DIVISIONS</h2>
<div class="div-sub abs">What We Offer</div>

<div class="card card-finance abs">
  <div class="icon-circle"><svg width="40" height="40" viewBox="0 0 40 40" fill="none" stroke="#fff" stroke-width="2"><circle cx="16" cy="22" r="11"/><path d="M16 16v12M19 18h-5a2 2 0 0 0 0 4h4a2 2 0 0 1 0 4h-5"/><rect x="24" y="18" width="12" height="16" rx="1"/><path d="M27 22h6M27 26h2M31 26h2M27 30h2M31 30h2"/></svg></div>
  <h3>Finance</h3>
  <p>With Wall Street’s fast-paced dynamic and ever-changing environment</p>
</div>
<div class="card card-health abs">
  <div class="icon-circle"><svg width="40" height="40" viewBox="0 0 40 40" fill="none" stroke="#1c1b5c" stroke-width="2"><rect x="5" y="12" width="30" height="20" rx="2"/><path d="M15 12V8h10v4M5 18l15 6 15-6"/><circle cx="20" cy="20" r="4"/></svg></div>
  <h3>Healthcare</h3>
  <p>Not only do we provide services to the finance and technology world</p>
</div>
<div class="card card-gov abs">
  <div class="icon-circle"><svg width="40" height="40" viewBox="0 0 40 40" fill="none" stroke="#fff" stroke-width="2"><path d="M5 14L20 6l15 8zM7 14h26M10 16v14M16 16v14M24 16v14M30 16v14M6 32h28M5 35h30"/></svg></div>
  <h3>Government Projects</h3>
  <p>Navigating the rules and regulations of Government integrators</p>
</div>

<!-- services -->
<h2 class="svc-title abs"><span>OUR</span> SERVICES</h2>
<article class="svc abs" style="left:146px">
  <div class="svc-photo" role="img" aria-label="Photo of two colleagues reviewing a tablet" style="background:linear-gradient(135deg,#dfe6ee,#4a5576)"></div>
  <h3>Hire Top<br>Professionals SDETs</h3>
  <p>We work with elite test-automation engineers. As a network, we have a very rigorous screening process to identify the</p>
  <a class="btn btn-more">View More</a>
</article>
<article class="svc abs" style="left:460px">
  <div class="svc-photo" role="img" aria-label="Photo of a professional woman seated at a desk" style="background:linear-gradient(135deg,#b9a58c,#2e3048)"></div>
  <h3>Let Us Build End to End<br>Automated QA Infrastructure</h3>
  <p>We can safe your time and budget. Our team will build and to end automated QA infrastructure for you. We work with latest</p>
  <a class="btn btn-more">View More</a>
</article>
<article class="svc abs" style="left:772px">
  <div class="svc-photo" role="img" aria-label="Photo of a senior executive in a meeting with a colleague" style="background:linear-gradient(135deg,#c9d6de,#3a3d52)"></div>
  <h3>Request Instructor For<br>your Team</h3>
  <p>We are committed to helping companies find the best instructors. Brightlane Staff has been successful in helping</p>
  <a class="btn btn-more">View More</a>
</article>

<!-- request a call -->
<div class="req-left abs" role="img" aria-label="Photo of an empty conference room, tinted navy"></div>
<div class="req-right abs" role="img" aria-label="Photo of an office meeting room, tinted orange"></div>
<svg class="band" style="top:2650px" width="1200" height="72" viewBox="0 0 1200 72">
  <polygon points="0,70 600,4 1200,70 1200,72 0,72" fill="var(--navy-deep)"/>
  <polygon points="597,72 597,22 1200,80" fill="var(--orange-soft)"/>
  <polygon points="0,72 597,14 597,72" fill="#2a2966"/>
</svg>
<h2 class="req-title abs">REQUEST A CALL</h2>
<p class="req-sub abs">Request a call from us to discuss our services and price estimation</p>
<div class="contact-item abs" style="top:2963px">
  <span class="pin"><svg width="18" height="18" viewBox="0 0 24 24" fill="none" stroke="#fff" stroke-width="2"><path d="M12 22s7-7 7-12a7 7 0 0 0-14 0c0 5 7 12 7 12z"/><circle cx="12" cy="10" r="2.5"/></svg></span>
  <div><small>Address</small><strong>2450 Harbor Ave, Fairfax, VA</strong></div>
</div>
<div class="contact-item abs" style="top:3043px">
  <span class="pin"><svg width="18" height="18" viewBox="0 0 24 24" fill="none" stroke="#fff" stroke-width="2"><rect x="3" y="5" width="18" height="14" rx="2"/><path d="M3 7l9 6 9-6"/></svg></span>
  <div><small>Email Address</small><strong>info@brightlanestaff.us</strong></div>
</div>
<div class="field abs" style="left:663px;top:2855px;width:184px">First Name</div>
<div class="field abs" style="left:886px;top:2855px;width:203px">Last Name</div>
<div class="field abs" style="left:663px;top:2907px;width:184px">Email address</div>
<div class="field abs" style="left:886px;top:2907px;width:203px">Phone</div>
<div class="field abs" style="left:663px;top:2966px;width:426px;padding-bottom:14px">Message</div>
<a class="btn btn-request abs">Request</a>

<!-- footer -->
<footer class="site-footer">
  <span class="social abs" style="left:146px"></span>
  <span class="social abs" style="left:181px"></span>
  <span class="social abs" style="left:217px"></span>
  <span class="social abs" style="left:253px"></span>
  <span class="social abs" style="left:290px"></span>
  <div class="brand abs"><span class="brand-mark"></span>BRIGHTLANE STAFF</div>
  <p class="copy abs">© 2022 Copyright: <span>Brightlane Staff, LLC</span><br>All rights reserved</p>
</footer>

</body>
</html>
```